Business Card Design

We are a commercial real estate brokerage in San Francisco, leasing office buildings downtown.
I would like a clean, elegant look. Simple but powerful .

Industry/Entity Type

Business

Contact Information for Business Card

Colin Farrow
lic# 07281549
415.555.0172
colin@tarvo-commercial.example
tarvo-commercial.example

```html
<!DOCTYPE html>
<html lang="en">
<head>
<meta charset="utf-8">
<title>Tarvo Commercial – Business Card</title>
<link href="https://fonts.googleapis.com/css2?family=Montserrat:wght@400;500&family=Open+Sans:wght@400&display=swap" rel="stylesheet">
<style>
  :root {
    --backdrop: #e4e6ea;
    --card: #f7f7f7;
    --accent: #7486a6;
    --ink: #4a4d52;
    --rule: #5d6066;
    --mark: #8d9099;
  }
  * { margin: 0; padding: 0; box-sizing: border-box; }
  html, body {
    width: 1200px; height: 675px; overflow: hidden;
    background: var(--backdrop);
  }
  .card {
    position: absolute; left: 75px; top: 37px;
    width: 1050px; height: 600px;
    background: var(--card);
    box-shadow: 0 6px 24px rgba(0,0,0,0.12);
  }
  .brand {
    position: absolute; left: 120px; top: 250px;
    display: flex; align-items: center; gap: 22px;
  }
  .brand-square { width: 86px; height: 86px; background: var(--mark); }
  .brand-divider { width: 2px; height: 90px; background: var(--rule); }
  .brand-name {
    font-family: "Montserrat", sans-serif; font-weight: 500;
    color: var(--accent); text-transform: uppercase; line-height: 1;
  }
  .brand-name .primary { display: block; font-size: 60px; letter-spacing: 2px; }
  .brand-name .secondary { display: block; font-size: 25px; letter-spacing: 2.5px; margin-top: 6px; }
  .card-divider {
    position: absolute; left: 540px; top: 80px;
    width: 1.5px; height: 440px; background: var(--rule);
  }
  .license {
    position: absolute; right: 70px; top: 50px;
    font-family: "Open Sans", sans-serif; font-size: 15px; color: var(--ink);
  }
  .contact { position: absolute; left: 600px; top: 220px; }
  .contact-name {
    font-family: "Montserrat", sans-serif; font-weight: 400;
    font-size: 34px; letter-spacing: 1px; color: var(--accent);
    text-transform: uppercase; margin-bottom: 14px;
  }
  .contact-list { list-style: none; }
  .contact-item {
    display: flex; align-items: center; gap: 14px;
    font-family: "Open Sans", sans-serif; font-size: 19px;
    color: var(--ink); line-height: 34px;
  }
  .contact-icon { width: 18px; height: 18px; flex: none; }
  .contact-icon * { fill: none; stroke: var(--accent); stroke-width: 1.8; }
  .contact-icon .solid { fill: var(--accent); stroke: none; }
</style>
</head>
<body>
  <div class="card">
    <div class="brand">
      <div class="brand-square"></div>
      <div class="brand-divider"></div>
      <div class="brand-name">
        <span class="primary">Tarvo</span>
        <span class="secondary">Commercial</span>
      </div>
    </div>

    <div class="card-divider"></div>

    <p class="license">Lic # 07281549</p>

    <div class="contact">
      <h1 class="contact-name">Colin Farrow</h1>
      <ul class="contact-list">
        <li class="contact-item">
          <svg class="contact-icon" viewBox="0 0 18 18" aria-hidden="true">
            <path class="solid" d="M4 1.5l3 3.2-1.6 2a10 10 0 0 0 5.9 5.9l2-1.6 3.2 3-1.8 2.4C8 16 2 10 1.6 3.3z"/>
          </svg>
          <span>415.555.0172</span>
        </li>
        <li class="contact-item">
          <svg class="contact-icon" viewBox="0 0 18 18" aria-hidden="true">
            <rect x="1.5" y="3.5" width="15" height="11"/>
            <path d="M1.5 3.5l7.5 6 7.5-6"/>
          </svg>
          <span>colin@tarvo-commercial.example</span>
        </li>
        <li class="contact-item">
          <svg class="contact-icon" viewBox="0 0 18 18" aria-hidden="true">
            <circle cx="9" cy="9" r="7.5"/>
            <ellipse cx="9" cy="9" rx="3.2" ry="7.5"/>
            <path d="M1.5 9h15"/>
          </svg>
          <span>www.tarvo-commercial.example</span>
        </li>
      </ul>
    </div>
  </div>
</body>
</html>
```